Basic business card

use my newly created logo - and the phrases (Smarter Chip Validation & Faster Silicon Launch Readiness) - and my new email domain / ID - use at conferences / tradeshows

Industry/Entity Type

semiconductor

Contact Information for Business Card

Dale J Whitcomb, Owner, communicate via Logo - Lower COT - Cost of Test, Accelerated NPI - New Product Introduction, phone +1 555 014 6208, Larkmoor, Nevada, USA, dale.whitcomb@vexlora.com

Font styles to use
Sans Serif

Requirements
Nice to have
• re-use my logo created via Pixel Harbor last August (#6182935)

```html
<!DOCTYPE html>
<html lang="en">
<head>
<meta charset="utf-8">
<title>Vexlora Business Card</title>
<link rel="stylesheet" href="https://fonts.googleapis.com/css2?family=Montserrat:wght@400;500;700&display=swap">
<style>
  :root {
    --bg: #c4c4c4;
    --navy: #4a5872;
    --white: #ffffff;
    --sky: #3bb4e5;
    --green: #7ab52a;
    --orange: #f0901e;
    --mail-blue: #1f6fc0;
    --slate-light: #8a97b0;
    --text-dark: #3f4c66;
  }
  * { margin: 0; padding: 0; box-sizing: border-box; }
  html, body { width: 1200px; height: 788px; overflow: hidden; }
  body {
    background: var(--bg);
    font-family: "Montserrat", sans-serif;
    position: relative;
  }
  .card {
    position: absolute;
    top: 244px;
    width: 525px;
    height: 300px;
    border-radius: 24px;
    overflow: hidden;
    box-shadow: 0 10px 28px rgba(0,0,0,0.25);
  }
  .card-front { left: 50px; background: var(--white); }
  .card-back { left: 625px; background: var(--navy); }
  .front-shape { position: absolute; inset: 0; }
  .brand {
    position: absolute;
    display: flex;
    align-items: center;
    gap: 10px;
    color: var(--text-dark);
    font-weight: 500;
    white-space: nowrap;
  }
  .brand-mark { display: block; background: currentColor; }
  .card-front .brand { left: 34px; top: 104px; font-size: 32px; letter-spacing: 1px; }
  .card-front .brand-mark { width: 14px; height: 14px; }
  .divider {
    position: absolute; left: 222px; top: 56px;
    width: 1px; height: 110px; background: var(--text-dark); opacity: 0.7;
  }
  .contact { position: absolute; left: 240px; top: 48px; color: var(--text-dark); white-space: nowrap; }
  .contact-name { font-weight: 700; font-size: 20px; line-height: 1.1; }
  .contact-role { font-size: 12px; margin-top: 3px; margin-bottom: 14px; }
  .contact-line {
    display: flex; align-items: center; gap: 6px;
    font-size: 11px; line-height: 20px;
  }
  .contact-line svg { width: 11px; height: 11px; flex: none; }
  .card-back .brand {
    left: 90px; top: 100px; font-size: 62px; letter-spacing: 2px;
    color: var(--slate-light); gap: 16px;
  }
  .card-back .brand-mark { width: 26px; height: 26px; }
  .tagline {
    position: absolute; left: 0; right: 0; bottom: 46px;
    text-align: center; font-size: 13px; color: var(--white);
    letter-spacing: 0.3px; white-space: nowrap;
  }
  .tone-sky { color: var(--sky); }
  .tone-green { color: var(--green); }
</style>
</head>
<body>
  <section class="card card-front">
    <svg class="front-shape" viewBox="0 0 525 300" width="525" height="300" aria-hidden="true">
      <path d="M70 300 C260 292 470 220 525 60 L525 300 Z" fill="var(--navy)"/>
      <g transform="translate(-6 -6)" fill="none" stroke-width="5">
        <path d="M70 300 C260 292 470 220 525 60" pathLength="100" stroke="var(--sky)" stroke-dasharray="38 100"/>
        <path d="M70 300 C260 292 470 220 525 60" pathLength="100" stroke="var(--green)" stroke-dasharray="0 66 34 10"/>
      </g>
    </svg>
    <div class="brand"><span class="brand-mark"></span>Vexlora</div>
    <div class="divider"></div>
    <div class="contact">
      <div class="contact-name">Dale J Whitcomb</div>
      <div class="contact-role">Owner</div>
      <div class="contact-line">
        <svg viewBox="0 0 12 12"><path d="M2 1 L4.5 1 L5.5 3.5 L4 4.6 C4.8 6.3 5.7 7.2 7.4 8 L8.5 6.5 L11 7.5 L11 10 C11 10.6 10.6 11 10 11 C5 11 1 7 1 2 C1 1.4 1.4 1 2 1 Z" fill="var(--orange)"/></svg>
        +1 555 014 6208
      </div>
      <div class="contact-line">
        <svg viewBox="0 0 12 12"><rect x="0.5" y="2" width="11" height="8" fill="var(--mail-blue)"/><path d="M0.5 2 L6 6.5 L11.5 2 M0.5 10 L4.5 6 M11.5 10 L7.5 6" stroke="#fff" stroke-width="1" fill="none"/></svg>
        dale.whitcomb@vexlora.com
      </div>
      <div class="contact-line">
        <svg viewBox="0 0 12 12"><path d="M6 11.5 C3 7.8 2 6 2 4.4 A4 4 0 0 1 10 4.4 C10 6 9 7.8 6 11.5 Z" fill="var(--green)"/><circle cx="6" cy="4.4" r="1.6" fill="#fff"/></svg>
        Larkmoor, Nevada, USA
      </div>
    </div>
  </section>

  <section class="card card-back">
    <div class="brand"><span class="brand-mark"></span>Vexlora</div>
    <p class="tagline">Smarter <span class="tone-sky">Chip Validation</span> &amp; Faster <span class="tone-green">Silicon Launch Readiness</span></p>
  </section>
</body>
</html>
```